Lorabelle Hair Flyer - tri-fold

I have added 2 participation payments to the project. I am not sure how I allocate them, but I would like to award them to two particular designers. When I find out how to do it I will allocate them. Thank you to everyone that participated, most designs were outstanding, and it was very hard to chose a winner.
========================================
PLEASE NO NEW DESIGNERS. I HAVE ENOUGH GOOD DESIGNS NOW, THAT I WILL WORK WITH ON THE EXISTING DESIGNERS. THANK YOU FOR ALL PARTICIPATING. THE QUALITY OF ALL SUBMISSIONS HAS EXCEEDED MY EXPECTATIONS, AND IS MAKING THE CHOICE DIFFICULT.
==============================================================

I have attached a proof pdf which is my draft design (I just used a stock template from Printorra) to do the mock up.

I would like you to replace the 3 main pictures of models with those I have attached. The name of the files will tell you where they should go.
I have attached pictures of all the stock photos as well, and most of the text is in the text file to save you typing it in.

I want the background colour to match Lorabelle colours so black with a fade to gold or something like that, must look sophisticated. I have attached Lorabelle logo files in black and white background.

The main pictures I have attached from the models will need to be blended into the background as well, but the hair still needs to be visible (might be hard given it is black hair as well,). The title stripes should be a gold fade as well, and the lorabelle text should be replaced with our logo.

please also add in the Facebook and WhatsApp logo's in the appropriate places. The dimensions should be 279mm * 216mm and print in the PrintOrra tri-fold brochure.

Possible ongoing work for the winning person, as the original designer of the logo only does logos/business cards, not other print material. Have logos in other formats (ai/cdr/jpeg) if required

Target Market(s)

African women

Industry/Entity Type

Hair

Font styles to use
Serif

Requirements
Must have
• Logo, product pictures, attached text, layout changes to draft mock up is ok if it looks better. Must conform to Printorra tri-fold layout
Nice to have
• Based on logo colours, black, white, gold complimentary colours to that palette are ok

```html
<!DOCTYPE html>
<html lang="en">
<head>
<meta charset="utf-8">
<title>Lorabelle Hair – Our Product</title>
<link href="https://fonts.googleapis.com/css2?family=Cinzel:wght@700&family=Marcellus&family=Montserrat:wght@400;500&family=Raleway:wght@500&display=swap" rel="stylesheet">
<style>
  :root {
    --ink: #050505;
    --gold: #d8b85a;
    --gold-deep: #9a7a2c;
    --gold-light: #f2dc96;
    --white: #ffffff;
    --soft-white: #e9e9e9;
    --band: rgba(90, 90, 90, 0.35);
    --hair-dark: #1a110c;
    --hair-mid: #3b271b;
    --skin: #9a6444;
    --skin-deep: #6e4229;
  }
  * { margin: 0; padding: 0; box-sizing: border-box; }
  html, body { width: 1200px; height: 848px; overflow: hidden; background: var(--ink); }
  .flyer {
    position: relative;
    width: 1200px; height: 848px;
    overflow: hidden;
    background:
      radial-gradient(circle at 560px 20px, rgba(216,184,90,0.18), transparent 180px),
      radial-gradient(circle at 300px 520px, rgba(80,80,80,0.35), transparent 420px),
      linear-gradient(160deg, #1a1a1a 0%, var(--ink) 45%, #0c0c0c 100%);
    font-family: "Montserrat", sans-serif;
    color: var(--white);
  }
  .portrait {
    position: absolute;
    left: 560px; top: 0;
    width: 640px; height: 848px;
    background:
      radial-gradient(ellipse 210px 300px at 420px 560px, var(--skin) 0%, var(--skin-deep) 55%, transparent 85%),
      radial-gradient(ellipse 420px 520px at 420px 340px, var(--hair-mid) 0%, var(--hair-dark) 70%, transparent 100%),
      linear-gradient(180deg, var(--hair-mid) 0%, var(--hair-dark) 60%, #2a1a12 100%);
    -webkit-mask-image: linear-gradient(90deg, transparent 0%, rgba(0,0,0,0.6) 22%, #000 40%);
            mask-image: linear-gradient(90deg, transparent 0%, rgba(0,0,0,0.6) 22%, #000 40%);
  }
  .section-title {
    position: absolute;
    left: 40px; top: 40px;
    font-family: "Cinzel", serif;
    font-weight: 700;
    font-size: 27px;
    letter-spacing: 1px;
    color: var(--gold);
  }
  .intro {
    position: absolute;
    left: 43px; top: 86px;
    font-size: 20px;
    letter-spacing: 0.8px;
    color: var(--soft-white);
  }
  .style-card { position: absolute; width: 134px; }
  .style-frame {
    width: 134px; height: 130px;
    padding: 5px;
    border-radius: 6px 44px 6px 44px;
    background: linear-gradient(135deg, var(--gold-light), var(--gold-deep) 55%, var(--gold));
    box-shadow: 0 3px 8px rgba(0,0,0,0.6);
  }
  .style-photo {
    width: 100%; height: 100%;
    border-radius: 3px 40px 3px 40px;
    background: radial-gradient(ellipse at 50% 50%, #2a2a2a 0%, #3c3c3c 35%, #f4f4f4 72%);
  }
  .style-name {
    margin-top: 18px;
    text-align: center;
    font-size: 15px;
    letter-spacing: 1px;
    color: var(--soft-white);
    white-space: nowrap;
  }
  .note {
    position: absolute;
    left: 48px; top: 490px;
    width: 660px;
    font-size: 16.5px;
    line-height: 20px;
    letter-spacing: 0.6px;
    color: var(--gold);
  }
  .note svg { position: absolute; left: 0; top: 4px; }
  .note p { padding-left: 29px; }
  .ranges-head {
    position: absolute;
    left: 42px; top: 558px;
    width: 680px;
    display: flex; align-items: center; gap: 10px;
  }
  .ranges-head h2 {
    font-family: "Marcellus", serif;
    font-weight: 400;
    font-size: 30px;
    color: var(--gold-light);
  }
  .ranges-head .rule { flex: 1; height: 1px; background: var(--soft-white); margin-top: 6px; }
  .ranges-copy {
    position: absolute;
    left: 45px; top: 602px;
    width: 686px;
    font-family: "Raleway", sans-serif;
    font-weight: 500;
    font-size: 15.5px;
    line-height: 20.5px;
    color: var(--white);
  }
  .ranges-copy p { margin-bottom: 10px; }
  .footer-band {
    position: absolute;
    left: 0; top: 800px;
    width: 1200px; height: 24px;
    background: linear-gradient(90deg, transparent 0%, var(--band) 20%, var(--band) 100%);
  }
  .brand {
    position: absolute;
    left: 40px; top: 798px;
    display: flex; align-items: center; gap: 6px;
  }
  .brand-mark { width: 9px; height: 9px; border-radius: 50%; background: var(--gold); }
  .brand-name {
    font-family: "Montserrat", sans-serif;
    font-weight: 500;
    font-size: 16px;
    color: var(--white);
    letter-spacing: 0.5px;
  }
  .brand-tag {
    position: absolute;
    left: 56px; top: 818px;
    font-size: 6px;
    color: var(--soft-white);
  }
  .web {
    position: absolute;
    right: 20px; top: 801px;
    font-size: 17px;
    letter-spacing: 1.6px;
    color: var(--white);
  }
</style>
</head>
<body>
<main class="flyer">
  <div class="portrait" role="img" aria-label="Portrait of a smiling woman with voluminous dark curly hair and long sparkling earrings"></div>

  <h1 class="section-title">OUR PRODUCT</h1>
  <p class="intro">We Provide natural 100g Wefts in the following styles</p>

  <div class="style-card" style="left:46px; top:136px;">
    <div class="style-frame"><div class="style-photo" role="img" aria-label="Straight hair weft"></div></div>
    <div class="style-name">Straight</div>
  </div>
  <div class="style-card" style="left:206px; top:136px;">
    <div class="style-frame"><div class="style-photo" role="img" aria-label="Body wave hair bundles"></div></div>
    <div class="style-name">Body Wave</div>
  </div>
  <div class="style-card" style="left:432px; top:136px;">
    <div class="style-frame"><div class="style-photo" role="img" aria-label="Romance curl hair bundles"></div></div>
    <div class="style-name">Romance Curl</div>
  </div>
  <div class="style-card" style="left:592px; top:136px;">
    <div class="style-frame"><div class="style-photo" role="img" aria-label="Kinky curl hair bundles"></div></div>
    <div class="style-name">Kinky Curl</div>
  </div>

  <div class="style-card" style="left:46px; top:306px;">
    <div class="style-frame"><div class="style-photo" role="img" aria-label="Deep wave hair bundles"></div></div>
    <div class="style-name">Deep Wave</div>
  </div>
  <div class="style-card" style="left:206px; top:306px;">
    <div class="style-frame"><div class="style-photo" role="img" aria-label="Fumi curl hair bundles"></div></div>
    <div class="style-name">Fumi Curl</div>
  </div>
  <div class="style-card" style="left:432px; top:306px;">
    <div class="style-frame"><div class="style-photo" role="img" aria-label="Jerry curl hair bundles"></div></div>
    <div class="style-name">Jerry Curl</div>
  </div>
  <div class="style-card" style="left:592px; top:306px;">
    <div class="style-frame"><div class="style-photo" role="img" aria-label="Body wave lace closure"></div></div>
    <div class="style-name">Matching Closures</div>
  </div>

  <div class="note">
    <svg width="18" height="12" viewBox="0 0 18 12" aria-hidden="true">
      <path d="M0 12V7C0 3 2 1 6 0l1 2C5 3 4 4 4 6h3v6zM10 12V7c0-4 2-6 6-7l1 2c-2 1-3 2-3 4h3v6z" fill="var(--gold)"/>
    </svg>
    <p>Ask about our other styles and options. We sell 360 Degree Closures, and we can sell Ombre and blonde tip hair as well. Speak to your&nbsp; Sales Consultant if there are other styles you are interested in. ”</p>
  </div>

  <div class="ranges-head">
    <h2>Ranges</h2>
    <span class="rule"></span>
  </div>
  <div class="ranges-copy">
    <p>We have two ranges to give our customers choice, our Platinum range is sourced from India and comes from a single donor.</p>
    <p>Our Premium range is sourced from donors from Asia and are typically referred to as Brazilian or Peruvian in the Industry.</p>
    <p>Both are 100% Virgin Remy hair. Both come with a 1 year Warranty, both are the highest quality hair in the industry</p>
  </div>

  <div class="footer-band"></div>
  <div class="brand">
    <span class="brand-mark"></span>
    <span class="brand-name">Lorabelle</span>
  </div>
  <div class="brand-tag">100% Human Hair</div>
  <div class="web">www.lorabellehair.com</div>
</main>
</body>
</html>
```